VARSEK MOBILE APP RE-DESIGN - MINIMALISTIC AND CLEAN DESIGN

We are looking for a design that is minimalistic, clean, modern and appealing to millennials...
IMPORTANT: This is NOT a logo design nor a website design... This is for a mobile App Design. You can download our app on iOS or Android: "VARSEK eLINKUP"

We are attaching our new logo and some apps that we like the design, colors, shadows, 3d effects, style, etc...

For content, you can check our website: www.varsek-app.example

Please feel free to ask questions, it's very important that you understand the project. Thank you

Also, check out this website...we do like the design and colors: https://brontil-demo.example/
Updates

This is not for a logo design... this is for a mobile app design.... please download our app on iOS: VARSEK eLINKUP... THANK YOU

Target Market(s)

20 - 35
60% Male 40 Female

Requirements
Must have
• great graphics, color shadows for 3d effects, great colors with transparency, IMPORTANT: CLEAN DESIGN, Minimalistic.

```html
<!DOCTYPE html>
<html lang="en">
<head>
<meta charset="utf-8">
<title>Varsek — Mobile App Screens</title>
<link rel="stylesheet" href="https://fonts.googleapis.com/css2?family=Montserrat:wght@400;500;600;700&display=swap">
<style>
:root{
  --bg:#e8ebef;
  --screen:#ffffff;
  --ink:#1d1f2b;
  --muted:#8a8f9c;
  --line:#d9dce2;
  --blue:#3d8fe6;
  --indigo:#4a3db5;
  --sky:#5ab4f0;
  --star:#f39a1e;
  --seal:#e4e7ee;
  --red:#e3264a;
  --soft:#f3f4f7;
  --grad:linear-gradient(135deg,var(--sky),var(--indigo));
}
*{box-sizing:border-box;margin:0;padding:0}
html,body{width:1200px;height:1109px;overflow:hidden}
body{background:var(--bg);font-family:"Montserrat",sans-serif;color:var(--ink);position:relative}
.brand{position:absolute;left:60px;top:50px;display:flex;align-items:center;gap:18px}
.brand-dot{width:64px;height:64px;border-radius:50%;background:var(--grad)}
.brand-name{font-size:64px;font-weight:600;letter-spacing:-1px;color:var(--ink)}
.screen{position:absolute;width:262px;height:440px;background:var(--screen);border-radius:30px;
  box-shadow:0 18px 40px rgba(60,70,110,.14);overflow:hidden;font-size:9px}
.r1{top:170px}.r2{top:640px}
.c1{left:40px}.c2{left:322px}.c3{left:604px}.c4{left:886px}
.nav{position:absolute;left:0;right:0;bottom:0;height:54px;display:flex;justify-content:space-around;align-items:center;
  background:#fff;border-top:1px solid var(--soft);font-size:6.5px;color:var(--muted);text-transform:uppercase;letter-spacing:.3px}
.nav span{display:flex;flex-direction:column;align-items:center;gap:3px}
.nav i{width:12px;height:12px;border:1.6px solid var(--ink);border-radius:3px;display:block}
.nav .home{color:var(--blue)} .nav .home i{border-color:var(--blue)}
.nav .hub{width:34px;height:34px;border-radius:50%;background:var(--grad);box-shadow:0 6px 14px rgba(74,61,181,.35)}
/* splash */
.splash{display:flex;flex-direction:column;align-items:center;justify-content:center;gap:26px}
.splash .brand-dot{width:44px;height:44px}
.splash .wordmark{font-size:34px;font-weight:600;display:flex;align-items:center;gap:10px}
/* auth */
.blob{position:absolute;top:0;right:0}
.auth{padding:70px 26px 0}
.auth h2{font-size:15px;font-weight:500;line-height:1.2}
.auth h2 b{display:block;font-size:22px;font-weight:600}
.field{margin-top:22px;font-size:8px;color:var(--muted);border-bottom:1px solid var(--line);padding-bottom:14px}
.field.active{border-bottom-color:var(--sky)}
.pill{margin:26px 0 0 auto;width:120px;height:34px;border-radius:17px;background:var(--grad);color:#fff;font-size:10px;font-weight:600;
  display:flex;align-items:center;justify-content:center;box-shadow:0 10px 20px rgba(74,61,181,.3)}
.aside{font-size:8px;color:var(--blue);text-align:right;margin-top:10px}
.social{margin-top:26px;font-size:8px;color:var(--muted)}
.social-row{display:flex;gap:10px;margin-top:8px}
.social-row span{display:flex;align-items:center;gap:5px;font-size:9px;font-weight:600;color:var(--ink)}
.social-row span::before{content:"";width:14px;height:14px;border-radius:3px;background:var(--soft);border:1px solid var(--line)}
.foot{position:absolute;bottom:22px;left:26px;right:26px;font-size:8px;color:var(--muted)}
.foot b{color:var(--indigo);font-weight:700}
/* listing */
.pad{padding:34px 18px 0}
.title{font-size:22px;font-weight:400;line-height:1.05}
.search{height:26px;border-radius:13px;background:var(--soft);margin-top:10px}
.tabs{display:flex;gap:10px;font-size:7px;color:var(--muted);margin:10px 0 8px}
.tabs .on{color:var(--blue)}
.card{background:#fff;border-radius:14px;box-shadow:0 8px 20px rgba(60,70,110,.1);padding:10px;margin-bottom:10px;position:relative}
.card-head{display:flex;justify-content:space-between;align-items:flex-start;gap:8px}
.who{display:flex;align-items:center;gap:6px;font-weight:600;font-size:8.5px}
.who small{display:block;font-weight:400;color:var(--muted);font-size:6.5px}
.avatar{width:18px;height:18px;border-radius:50%;background:linear-gradient(135deg,#9aa3b5,#555e70);flex:none}
.note{font-size:6.5px;color:var(--muted);margin:5px 0;line-height:1.35}
.offer-row{display:flex;justify-content:space-between;align-items:center}
.offer{font-weight:700;font-size:9px}
.stars{color:var(--star);font-size:10px;letter-spacing:1px}
.stars em{font-style:normal;color:var(--ink);font-size:8px;margin-left:4px}
.credits{font-size:6.5px;color:var(--muted)}
.count{background:var(--sky);color:#fff;font-size:7px;border-radius:8px;padding:2px 6px;flex:none}
.seal{width:30px;height:30px;border-radius:50%;background:var(--seal);flex:none}
.seal.big{width:46px;height:46px}
.merchant{font-size:15px;font-weight:700;color:var(--sky);margin:3px 0}
/* detail */
.detail-head{display:flex;justify-content:space-between;align-items:flex-start}
.stat-row{display:flex;gap:6px;margin:8px 0}
.stat-row span{background:var(--grad);color:#fff;border-radius:10px;padding:3px 8px;font-size:7px;font-weight:600}
.label{font-size:6.5px;color:var(--muted);margin-top:6px}
.value{font-size:9px;font-weight:600}
.tag{display:inline-block;background:var(--red);color:#fff;font-size:6px;border-radius:6px;padding:1px 5px;margin-left:4px}
.bar{margin-top:10px;background:var(--soft);border-radius:12px;padding:8px 12px;font-size:8.5px;font-weight:700;display:flex;justify-content:space-between}
/* comments */
.comment{display:flex;gap:8px;margin-top:10px}
.comment p{font-size:7.5px;line-height:1.4}
.reply{margin-left:auto;background:var(--grad);color:#fff;font-size:7px;border-radius:9px;padding:3px 9px;align-self:flex-end}
/* profile */
.hero{height:150px;background:linear-gradient(160deg,#dfe1e6,#c9ccd3 60%,#e9c6cc)}
.hero-title{position:absolute;top:28px;left:20px;font-size:20px;font-weight:400;color:#fff}
.p-avatar{position:absolute;top:120px;left:18px;width:56px;height:56px;border-radius:50%;border:3px solid #fff;background:linear-gradient(135deg,#c9a78d,#6d5546)}
.p-name{position:absolute;top:150px;left:84px;font-size:10px;font-weight:700}
.p-name small{display:block;font-weight:400;font-size:6.5px;color:var(--muted)}
.premium{position:absolute;top:152px;right:16px;background:var(--sky);color:#fff;font-size:7px;border-radius:8px;padding:2px 7px}
.p-stats{position:absolute;top:190px;left:18px;right:18px;display:flex;justify-content:space-between}
.p-stats b{display:block;font-size:18px;font-weight:500}
.p-stats span{font-size:6.5px;color:var(--muted)}
.feed{position:absolute;top:245px;left:18px;right:18px}
.promo{height:100px;border-radius:12px;margin-top:8px;background:linear-gradient(135deg,#d8e65a,#6f9d2c);position:relative}
.promo b{position:absolute;right:12px;bottom:12px;color:#fff;font-size:13px;font-weight:700}
</style>
</head>
<body>

<header class="brand"><span class="brand-dot"></span><span class="brand-name">varsek</span></header>

<!-- Splash -->
<section class="screen splash r1 c1">
  <div class="wordmark"><span class="brand-dot"></span>varsek</div>
  <svg width="18" height="18" viewBox="0 0 18 18" aria-hidden="true"><circle cx="9" cy="9" r="7" fill="none" stroke="#5ab4f0" stroke-width="2" stroke-dasharray="2 3"/></svg>
</section>

<!-- Sign up -->
<section class="screen r1 c2">
  <svg class="blob" width="110" height="150" viewBox="0 0 110 150" aria-hidden="true"><defs><linearGradient id="g1" x1="0" y1="0" x2="1" y2="1"><stop offset="0" stop-color="#5ab4f0"/><stop offset="1" stop-color="#4a3db5"/></linearGradient></defs><path d="M40 0C50 50 20 70 40 110C60 150 110 140 110 140V0Z" fill="url(#g1)"/></svg>
  <div class="auth">
    <h2>Create account with<b>varsek</b></h2>
    <div class="field">E-mail address</div>
    <div class="field active">Password</div>
    <div class="field">Confirm password</div>
    <div class="pill">Sign up</div>
    <div class="social">Or Login with<div class="social-row"><span>Circlebook</span><span>Searchly</span></div></div>
  </div>
  <div class="foot">I do have an account, then <b>LOG IN</b></div>
</section>

<!-- Log in -->
<section class="screen r1 c3">
  <svg class="blob" width="110" height="150" viewBox="0 0 110 150" aria-hidden="true"><defs><linearGradient id="g2" x1="0" y1="0" x2="1" y2="1"><stop offset="0" stop-color="#5ab4f0"/><stop offset="1" stop-color="#4a3db5"/></linearGradient></defs><path d="M40 0C50 50 20 70 40 110C60 150 110 140 110 140V0Z" fill="url(#g2)"/></svg>
  <div class="auth">
    <h2>Welcome to<b>varsek</b></h2>
    <div class="field">Username</div>
    <div class="field active">Password</div>
    <div class="aside">Forgot password?</div>
    <div class="pill">Log in</div>
    <div class="social">Or Login with<div class="social-row"><span>Circlebook</span><span>Searchly</span></div></div>
  </div>
  <div class="foot">Don't have an account? <b>SIGN UP</b></div>
</section>

<!-- Featured listing -->
<section class="screen r1 c4">
  <div class="pad">
    <div class="title">Featured<br>Listing</div>
    <div class="search"></div>
    <div class="card" style="margin-top:10px">
      <div class="card-head">
        <div class="who"><span class="avatar" role="img" aria-label="User avatar"></span><div>Lotte van Aken<small>3 hours ago</small></div></div>
        <span class="seal" role="img" aria-label="Partner badge"></span>
      </div>
      <p class="note">Hey! Get $10 when you sign up for Tillbank using my referral! Get a premium black card and early direct deposits.</p>
      <div class="offer-row"><div class="offer">$50 Statement Credit</div><span class="count">05</span></div>
      <div class="stars">★★★★☆<em>4.5</em></div>
      <div class="credits">50 Credits</div>
    </div>
    <div class="tabs"><span class="on">Recently</span><span>Popular</span><span>Premium</span><span>Best Ratings</span></div>
    <div class="card">
      <div class="who"><span class="avatar" role="img" aria-label="User avatar"></span><div>Lotte van Aken<small>Just now</small></div></div>
      <div class="merchant">Orvio</div>
      <div class="offer-row"><div class="offer">$50 Statement Credit</div><span class="count">05</span></div>
      <div class="stars">★★★★☆<em>4.5</em></div>
    </div>
  </div>
  <nav class="nav"><span class="home"><i></i>Home</span><span><i></i>Messages</span><span class="hub"></span><span><i></i>Notification</span><span><i></i>Profile</span></nav>
</section>

<!-- Categories -->
<section class="screen r2 c1">
  <div class="pad">
    <div class="title">Categories</div>
    <p class="note">All Sort of Products and Services offered</p>
    <div class="tabs"><span class="on">Recently</span><span>Popular</span><span>Premium</span><span>Best Rated</span></div>
    <div class="card">
      <div class="who"><span class="avatar" role="img" aria-label="User avatar"></span><div>Lotte van Aken<small>Just now</small></div></div>
      <div class="merchant">Orvio</div>
      <div class="offer-row"><div class="offer">$50 Statement Credit</div><span class="count">05</span></div>
      <div class="stars">★★★★☆<em>4.5</em></div>
      <div class="credits">50 Credits</div>
    </div>
    <div class="card">
      <div class="who"><span class="avatar" role="img" aria-label="User avatar"></span><div>Tomas Reyna<small>2 hours ago</small></div></div>
      <div class="merchant" style="color:var(--indigo)">skylark</div>
      <div class="offer-row"><div class="offer">$50 Statement Credit</div><span class="count">05</span></div>
      <div class="stars">★★★★☆<em>4.5</em></div>
      <div class="credits">$50 off on first order</div>
    </div>
  </div>
  <nav class="nav"><span class="home"><i></i>Home</span><span><i></i>Messages</span><span class="hub"></span><span><i></i>Notification</span><span><i></i>Profile</span></nav>
</section>

<!-- Listing detail -->
<section class="screen r2 c2">
  <div class="pad">
    <div class="detail-head">
      <div>
        <div class="stars" style="margin-top:6px">★★★★☆<em>4.5 (1242)</em></div>
        <div class="stat-row"><span>2152</span><span>3152</span><span>5152</span></div>
      </div>
      <span class="seal big" role="img" aria-label="Partner badge"></span>
    </div>
    <div class="who"><span class="avatar" role="img" aria-label="User avatar"></span><div>Lotte van Aken<small>3 hours ago</small></div></div>
    <p class="note">Hey! Get $10 when you sign up for Tillbank using my referral! Get a premium black card and early direct deposits.</p>
    <div class="label">Link to</div><div class="value">Referral Link <span class="tag">Jun 14, 2019</span></div>
    <div class="label">Promotion</div><div class="value">$50 Statement Credit</div>
    <div class="label">Description</div><div class="value">Become a Norvale cardmember &amp; get extra $50 find out more</div>
    <div class="bar">18 comments <span>⌄</span></div>
  </div>
  <nav class="nav"><span class="home"><i></i>Home</span><span><i></i>Messages</span><span class="hub"></span><span><i></i>Notification</span><span><i></i>Profile</span></nav>
</section>

<!-- Comments -->
<section class="screen r2 c3">
  <div class="pad">
    <div class="label">Promotion</div><div class="value">$50 Statement Credit</div>
    <div class="label">Description</div><div class="value">Become a Norvale cardmember &amp; get extra $50 find out more</div>
    <div class="label">Special Instructions</div><div class="value">A mobile bank for Gen-Z that combines an app with a debit card. Shared accounts for parents with teens, and personal checking for individuals 18+</div>
    <div class="bar">18 comments <span>⌃</span></div>
    <div class="value" style="margin-top:12px">17 comments</div>
    <div class="label">Sort by: Date added ⌄</div>
    <div class="comment"><span class="avatar" role="img" aria-label="User avatar"></span><div><div class="value">Nadia Fell</div><div class="label" style="margin:0">2 hours ago</div><p>Wow! I didn't know that there is such a cool discount offer! You guys need to see that!</p><div class="label">♡ 2 &nbsp; 👍 21</div></div></div>
    <div class="comment"><span class="avatar" role="img" aria-label="User avatar"></span><div class="value">Iker Salcedo</div><span class="reply">Reply</span></div>
  </div>
  <nav class="nav"><span class="home"><i></i>Home</span><span><i></i>Messages</span><span class="hub"></span><span><i></i>Notification</span><span><i></i>Profile</span></nav>
</section>

<!-- Profile -->
<section class="screen r2 c4">
  <div class="hero" role="img" aria-label="Profile cover photo of a pink lily"></div>
  <h3 class="hero-title">Profile</h3>
  <span class="p-avatar" role="img" aria-label="Profile picture"></span>
  <div class="p-name">Lotte van Aken<small>Glasgow</small></div>
  <span class="premium">Premium</span>
  <div class="p-stats"><div><b>22</b><span>Products</span></div><div><b>122</b><span>Views</span></div><div><b>82</b><span>Likes</span></div><div><b>52</b><span>Favorites</span></div></div>
  <div class="feed">
    <div class="who"><span class="avatar" role="img" aria-label="User avatar"></span><div>Greta Wendt<small>Just now</small></div></div>
    <div class="promo" role="img" aria-label="Promotion photo of a sunny meadow"><b>Big Discount</b></div>
  </div>
  <nav class="nav"><span class="home"><i></i>Home</span><span><i></i>Messages</span><span class="hub"></span><span><i></i>Notification</span><span><i></i>Profile</span></nav>
</section>

</body>
</html>
```